Afternoon Soiree Garden Party Invitation

Invitation design for an 'Afternoon Soirée' backyard garden party.
Format is for-print and mailing and can be either double-sided design to be enveloped and mailed or it can be a postcard-style with design on one side and address/postage placeholder on the reverse side.
Text, dimensions and additional information in the provided Word document.
Font styles to use
Script
Requirements
Must have
- Elegant, yet easy-going and warm/welcoming feel

```html
<!DOCTYPE html>
<html lang="en">
<head>
<meta charset="utf-8">
<title>An Afternoon Soiree Invitation</title>
<link rel="stylesheet" href="https://fonts.googleapis.com/css2?family=Great+Vibes&family=Amatic+SC:wght@700&family=Special+Elite&display=swap">
<style>
  :root {
    --page-bg: #e9e7e3;
    --night-teal: #1e3838;
    --dusk-slate: #445149;
    --meadow-sand: #a59f78;
    --ink-light: #f6f3ea;
    --ink-dark: #26322d;
    --leaf-deep: #3f5d4c;
    --leaf-soft: #7f9f86;
    --glow: rgba(255, 226, 150, 0.55);
  }
  * { margin: 0; padding: 0; box-sizing: border-box; }
  html, body { width: 1200px; height: 1200px; overflow: hidden; }
  body { background: var(--page-bg); position: relative; }

  .invitation {
    position: absolute;
    left: 230px; top: 70px;
    width: 740px; height: 1060px;
    background: linear-gradient(180deg, var(--night-teal) 0%, #263f3d 30%, var(--dusk-slate) 55%, #7d7c62 75%, var(--meadow-sand) 100%);
    overflow: hidden;
    box-shadow: 0 4px 14px rgba(0,0,0,0.18);
    color: var(--ink-light);
    text-align: center;
  }

  .string-lights {
    position: absolute; right: 0; top: 0;
    width: 400px; height: 190px;
    background: radial-gradient(ellipse at 70% 45%, var(--glow) 0%, rgba(255,226,150,0.12) 35%, transparent 70%);
  }

  .foliage-left {
    position: absolute; left: 0; bottom: 0;
    width: 360px; height: 470px;
    background: radial-gradient(ellipse at 15% 75%, var(--leaf-soft) 0%, var(--leaf-deep) 35%, rgba(63,93,76,0.35) 60%, transparent 75%);
  }
  .foliage-right {
    position: absolute; right: 0; bottom: 0;
    width: 460px; height: 170px;
    background: radial-gradient(ellipse at 60% 100%, var(--leaf-soft) 0%, rgba(63,93,76,0.6) 40%, transparent 75%);
  }

  .lead-in {
    position: absolute; top: 240px; width: 100%;
    font-family: "Amatic SC", sans-serif; font-size: 36px; letter-spacing: 2px;
  }
  .event-title {
    position: absolute; top: 330px; width: 100%;
    font-family: "Great Vibes", cursive; font-size: 76px; font-weight: 400;
  }

  .event-date {
    position: absolute; top: 490px; width: 100%;
    display: flex; justify-content: center; align-items: center; gap: 16px;
    font-family: "Special Elite", monospace;
  }
  .date-side {
    border-top: 1.5px solid var(--ink-light);
    border-bottom: 1.5px solid var(--ink-light);
    padding: 6px 8px; font-size: 26px; letter-spacing: 1px;
  }
  .date-day { display: flex; flex-direction: column; line-height: 0.9; }
  .date-month { font-size: 36px; }
  .date-number { font-size: 56px; }

  .venue-name {
    position: absolute; top: 612px; width: 100%;
    font-family: "Amatic SC", sans-serif; font-size: 48px; letter-spacing: 3px;
  }
  .venue-address {
    position: absolute; top: 668px; width: 100%;
    font-family: "Special Elite", monospace; font-size: 21px; letter-spacing: 1px;
  }

  .details {
    position: absolute; top: 800px; width: 100%;
    font-family: "Amatic SC", sans-serif; color: var(--ink-dark);
    font-size: 30px; letter-spacing: 2px; line-height: 40px;
  }
  .age-note {
    display: inline-block; margin-top: 12px;
    border-top: 1.5px solid var(--ink-dark);
    border-bottom: 1.5px solid var(--ink-dark);
    padding: 2px 20px; line-height: 40px;
  }
</style>
</head>
<body>
  <main class="invitation">
    <div class="string-lights" role="img" aria-label="Glowing string lights hanging across the top corner"></div>
    <div class="foliage-left" role="img" aria-label="Watercolour green leaves rising from the lower left"></div>
    <div class="foliage-right" role="img" aria-label="Watercolour green leaves along the lower right edge"></div>

    <p class="lead-in">Join us at</p>
    <h1 class="event-title">An Afternoon Soiree</h1>

    <div class="event-date">
      <span class="date-side">FRIDAY</span>
      <span class="date-day"><span class="date-month">Jul</span><span class="date-number">17</span></span>
      <span class="date-side">4-8 PM</span>
    </div>

    <p class="venue-name">The Marlowe Residence</p>
    <p class="venue-address">482 Brookfield Ave</p>

    <div class="details">
      <p>Weather permitting.</p>
      <p>Please call 555-214-7830 if unsure.</p>
      <p class="age-note">This is a 19+ event</p>
    </div>
  </main>
</body>
</html>
```